Banner for County Fair

Need a banner with our logo primarily, but some other color/background work. Also include city name West Point, NE. Tagline that could be used is Fiber Optic Fast! Also visit www.tolbrinkdata.com to get a feel for the company.

```html
<!DOCTYPE html>
<html lang="en">
<head>
<meta charset="utf-8">
<title>Tolbrink Banner</title>
<link href="https://fonts.googleapis.com/css2?family=Montserrat:ital,wght@0,600;0,700;0,800;1,800&display=swap" rel="stylesheet">
<style>
  :root {
    --page-bg: #e4e6e8;
    --banner-white: #f7f9fc;
    --brand-blue: #1679c4;
    --navy: #163a5c;
    --band-red: #ef5a5a;
    --band-blue: #17a8e6;
    --photo-cyan: #8fdcf2;
    --photo-deep: #1f7fc4;
    --white: #ffffff;
  }
  * { margin: 0; padding: 0; box-sizing: border-box; }
  html, body {
    width: 1200px; height: 1200px; overflow: hidden;
    background: var(--page-bg);
    font-family: "Montserrat", sans-serif;
  }
  .banner {
    position: absolute; left: 20px; top: 418px;
    width: 1160px; height: 365px;
    background: var(--banner-white);
    overflow: hidden;
    box-shadow: 0 10px 24px rgba(0,0,0,0.18);
  }
  .banner__photo {
    position: absolute; right: 0; top: 0;
    width: 620px; height: 365px;
    background:
      linear-gradient(90deg, var(--banner-white) 0%, rgba(247,249,252,0) 32%),
      radial-gradient(ellipse at 55% 40%, #e9fbff 0%, var(--photo-cyan) 35%, var(--photo-deep) 100%);
  }
  .brand {
    position: absolute; left: 100px; top: 62px;
    font-weight: 800; font-size: 108px; line-height: 1;
    letter-spacing: -3px; color: var(--brand-blue);
  }
  .tagline {
    position: absolute; left: 122px; top: 182px;
    font-weight: 800; font-style: italic; font-size: 42px;
    letter-spacing: 1px; color: var(--navy);
  }
  .city {
    position: absolute; left: 124px; top: 242px;
    font-weight: 700; font-size: 22px; letter-spacing: 2px;
    color: var(--navy);
  }
  .services {
    position: absolute; left: 0; top: 300px;
    width: 761px; height: 31px;
    background: var(--band-red);
    display: flex; align-items: center; justify-content: center; gap: 18px;
    padding-right: 60px;
    color: var(--white); font-weight: 700; font-size: 22px; letter-spacing: 0.5px;
  }
  .services__sep { font-weight: 600; opacity: 0.9; }
  .web {
    position: absolute; left: 761px; top: 300px;
    width: 399px; height: 31px;
    background: var(--band-blue);
    display: flex; align-items: center; padding-left: 12px;
    color: var(--white); font-weight: 700; font-size: 21px;
  }
</style>
</head>
<body>
  <div class="banner">
    <div class="banner__photo" role="img" aria-label="Photo of an open laptop showing a web address over streaks of fast-moving binary data"></div>
    <p class="brand">TOLBRINK</p>
    <p class="tagline">FIBER OPTIC FAST!</p>
    <p class="city">WEST POINT, NE</p>
    <div class="services">
      <span>NETWORK DESIGN</span><span class="services__sep">|</span>
      <span>INSTALLATION</span><span class="services__sep">|</span>
      <span>SUPPORT</span>
    </div>
    <div class="web">www.tolbrinkdata.com</div>
  </div>
</body>
</html>
```